Business Cards

Business cards (double-sided) to be handed out to clients and potential clients, with contact details, logo .

Target Market(s)

Small to medium size businesses

Industry/Entity Type

Accountants

Contact Information for Business Card

Brightmere Ledger Accounting & Advisory Ltd

Colors

Designer to choose only greyscale colors for use in the design.

Requirements
Must have
• Name, Title, Address, Phone number, Email, Website
Nice to have
• Modern, clean lines, classy
Should not have
• Business cards to be double-sided. Form keeps reverting to single-sided.

```html
<!DOCTYPE html>
<html lang="en">
<head>
<meta charset="utf-8">
<title>Brightmere Ledger – Business Cards</title>
<link rel="stylesheet" href="https://fonts.googleapis.com/css2?family=Josefin+Sans:wght@400&family=Roboto:wght@400;500&display=swap">
<style>
  :root {
    --backdrop: #2a2a2a;
    --paper: #ededed;
    --paper-light: #f4f4f4;
    --ink: #1a1a1a;
    --ink-soft: #2c2c2c;
    --band: #141414;
    --shade: #8a8a8a;
    --icon: #7a7a7a;
    --white: #f5f5f5;
  }
  html, body {
    margin: 0;
    padding: 0;
    width: 1200px;
    height: 1138px;
    overflow: hidden;
    background: var(--backdrop);
  }
  .canvas {
    position: relative;
    width: 1200px;
    height: 1138px;
  }
  .card {
    position: absolute;
    width: 622px;
    height: 374px;
    border-radius: 14px;
    overflow: hidden;
    background: linear-gradient(180deg, var(--paper-light), var(--paper));
  }
  .card--front { left: 272px; top: 184px; }
  .card--back  { left: 274px; top: 606px; }

  /* Front */
  .wordmark {
    position: absolute;
    left: 0;
    right: 0;
    top: 112px;
    text-align: center;
    font-family: "Josefin Sans", sans-serif;
    font-weight: 400;
    color: var(--ink);
  }
  .wordmark__name {
    display: block;
    font-size: 38px;
    letter-spacing: 3px;
    text-transform: uppercase;
    line-height: 1.1;
  }
  .wordmark__tagline {
    display: block;
    margin-top: 14px;
    font-size: 15px;
    letter-spacing: 3.5px;
    text-transform: uppercase;
  }
  .front-band {
    position: absolute;
    left: 0;
    right: 0;
    bottom: 0;
    height: 54px;
    background: var(--band);
    display: flex;
    align-items: center;
    justify-content: center;
    font-family: "Josefin Sans", sans-serif;
    font-size: 15px;
    letter-spacing: 3.5px;
    color: var(--white);
  }

  /* Back */
  .back-panel {
    position: absolute;
    inset: 0;
  }
  .contact {
    position: absolute;
    left: 52px;
    top: 82px;
    font-family: "Roboto", sans-serif;
    color: var(--ink-soft);
  }
  .contact__name {
    margin: 0;
    font-size: 23px;
    font-weight: 500;
    color: var(--ink);
    line-height: 1.2;
  }
  .contact__title {
    margin: 2px 0 0;
    font-size: 16px;
    line-height: 1.3;
  }
  .contact__list {
    list-style: none;
    margin: 30px 0 0;
    padding: 0;
    font-size: 16px;
  }
  .contact__item {
    display: flex;
    align-items: center;
    height: 24px;
  }
  .contact__icon {
    width: 14px;
    height: 14px;
    margin-right: 18px;
    fill: var(--icon);
  }
  .contact__address {
    margin: 8px 0 0;
    font-size: 16px;
    line-height: 24px;
  }
  .back-mark {
    position: absolute;
    left: 494px;
    top: 187px;
    width: 300px;
    transform: translate(-50%, -50%) rotate(-90deg);
    text-align: center;
    font-family: "Josefin Sans", sans-serif;
    font-weight: 400;
    color: var(--white);
    white-space: nowrap;
  }
  .back-mark__name {
    display: block;
    font-size: 22px;
    letter-spacing: 2px;
    text-transform: uppercase;
  }
  .back-mark__tagline {
    display: block;
    margin-top: 8px;
    font-size: 9.5px;
    letter-spacing: 2.5px;
    text-transform: uppercase;
  }
</style>
</head>
<body>
<main class="canvas">

  <section class="card card--front" aria-label="Card front">
    <div class="wordmark">
      <span class="wordmark__name">Brightmere Ledger</span>
      <span class="wordmark__tagline">Accounting &amp; Advisory</span>
    </div>
    <div class="front-band">www.BRIGHTMERELEDGER.com</div>
  </section>

  <section class="card card--back" aria-label="Card back">
    <svg class="back-panel" viewBox="0 0 622 374" preserveAspectRatio="none" aria-hidden="true">
      <path d="M406 0 C 340 60, 318 140, 318 187 C 318 250, 340 320, 410 374 L 396 374 C 330 320, 308 250, 308 187 C 308 130, 330 60, 392 0 Z" fill="var(--shade)"/>
      <path d="M406 0 C 350 60, 328 140, 328 187 C 328 250, 350 320, 410 374 L 622 374 L 622 0 Z" fill="var(--band)"/>
    </svg>

    <div class="contact">
      <h2 class="contact__name">Owen Hale Marsh</h2>
      <p class="contact__title">Managing Director</p>
      <ul class="contact__list">
        <li class="contact__item">
          <svg class="contact__icon" viewBox="0 0 16 16" aria-hidden="true"><path d="M2 5c0-2 3-3 6-3s6 1 6 3v1h-3V5H5v1H2z M4 7h8l2 6H2z"/></svg>
          555-014-2290
        </li>
        <li class="contact__item">
          <svg class="contact__icon" viewBox="0 0 16 16" aria-hidden="true"><path d="M1 3h14v10H1z M2 4l6 5 6-5v-.2H2z" fill-rule="evenodd"/></svg>
          owen@brightmereledger.com
        </li>
        <li class="contact__item">
          <svg class="contact__icon" viewBox="0 0 16 16" aria-hidden="true"><circle cx="8" cy="8" r="6.5" fill="none" stroke="var(--icon)" stroke-width="1.3"/><ellipse cx="8" cy="8" rx="2.6" ry="6.5" fill="none" stroke="var(--icon)" stroke-width="1.1"/><path d="M1.5 8h13" stroke="var(--icon)" stroke-width="1.1"/></svg>
          www.brightmereledger.com
        </li>
      </ul>
      <p class="contact__address">18 Harbour Row, Eastfield,<br>Northvale, US 204518</p>
    </div>

    <div class="back-mark">
      <span class="back-mark__name">Brightmere Ledger</span>
      <span class="back-mark__tagline">Accounting &amp; Advisory</span>
    </div>
  </section>

</main>
</body>
</html>
```